'Halbrook Video' - Website Template Design (that I can use in Word Press)

I would like a professional, colorful website template (4 pages) designed in a format that can be used with Word Press. Upon completion of the design, I would like to take over and maintain/host using Web Press and my Net Parrot account.

My business is videography - producing videos for companies, organizations and not-for-profit charities. Our company will do everything, including writing, planning, producing, directing filming and editing videos etc.

I have a colorful logo and business card already designed and I would like the website built around the look of the logo and business card.

I would like an index page designed first. Once the designer has created an index page I like best, I would like three more pages created with that same design.

1) A 'contact us' page
2) A page with a plug in that would allow me to upload video or connect to ClipVane to show samples of my videography
3) A general template page I could add new pages to in the future.

Target Market(s)

businesses of all kinds, organizations, governments, not-for-profit charities

Industry/Entity Type

Film Production

Number of Pages Required

4 page

Font styles to use
Sans Serif

Requirements
Must have
• 1) Index page
• 2) Contact Us page
• 2) A page with a plug in that would allow me to upload video or connect to ClipVane to show samples of my videography
• 3) A general template page I could add new pages to in the future
Nice to have
• Surprise me! I love lots of color and am open to creative ideas.

```html
<!DOCTYPE html>
<html lang="en">
<head>
<meta charset="utf-8">
<title>Halbrook Video</title>
<link href="https://fonts.googleapis.com/css2?family=Raleway:wght@500;600;700;800&family=Lato:wght@400;700&display=swap" rel="stylesheet">
<style>
  :root {
    --orange: #f26522;
    --ink: #1f1f1f;
    --text: #333333;
    --muted: #8a8a8a;
    --line: #d6d6d6;
    --band: #f4f4f4;
    --footer: #3b3b3b;
    --footer-line: #5a5a5a;
    --white: #ffffff;
  }
  * { box-sizing: border-box; margin: 0; padding: 0; }
  html, body { width: 861px; height: 1200px; overflow: hidden; }
  body { position: relative; background: var(--white); font-family: 'Lato', sans-serif; color: var(--text); }
  .abs { position: absolute; }

  /* Hero */
  .hero { left: 0; top: 0; width: 861px; height: 443px;
    background: linear-gradient(180deg, #d9d3c7 0%, #b49a72 35%, #7e6446 62%, #4a3a2c 100%); }
  .hero-glow { left: 0; top: 0; width: 861px; height: 443px;
    background: radial-gradient(ellipse at 75% 40%, rgba(255,226,170,.55), rgba(255,226,170,0) 60%); }
  .brand { left: 57px; top: 42px; display: flex; align-items: center; gap: 8px;
    font-family: 'Raleway', sans-serif; font-weight: 800; font-size: 19px; color: var(--ink); letter-spacing: .5px; }
  .brand-square { width: 22px; height: 22px; background: var(--orange); }
  .nav { right: 60px; top: 49px; display: flex; align-items: center; gap: 20px;
    font-family: 'Raleway', sans-serif; font-weight: 700; font-size: 12.5px; color: var(--ink); }
  .nav .active { color: var(--orange); border: 2px solid var(--orange); padding: 4px 12px; background: rgba(255,255,255,.85); }
  .headline { left: 0; top: 215px; width: 861px; text-align: center;
    font-family: 'Raleway', sans-serif; font-weight: 700; font-size: 25.5px; line-height: 31px;
    color: var(--white); text-shadow: 0 2px 6px rgba(0,0,0,.45); }
  .arrow { top: 226px; }

  /* Services */
  .services { left: 0; top: 443px; width: 861px; height: 260px; background: var(--band); }
  .section-title { font-family: 'Raleway', sans-serif; font-weight: 700; font-size: 20px; color: var(--ink); }
  .section-title span { color: var(--orange); }
  .services .section-title { left: 0; top: 26px; width: 861px; text-align: center; }
  .divider { top: 62px; height: 1px; background: #555; }
  .divider-mark { left: 424px; top: 57px; width: 11px; height: 11px; background: #9a9a9a; }
  .tile { top: 102px; width: 105px; height: 95px;
    background: linear-gradient(135deg, #f6dada 0%, #efe6dd 45%, #e6ecd9 75%, #dfe3ee 100%);
    display: flex; align-items: center; justify-content: center; }
  .tile-label { top: 215px; width: 150px; text-align: center;
    font-family: 'Raleway', sans-serif; font-weight: 600; font-size: 13px; color: var(--ink); }

  /* Welcome */
  .welcome-mark { left: 57px; top: 733px; width: 19px; height: 19px; background: var(--orange); }
  .welcome-title { left: 85px; top: 729px; }
  .rule { height: 1px; background: var(--line); }
  .intro { left: 58px; top: 774px; width: 466px; font-size: 10.4px; line-height: 15.3px; color: var(--ink); }
  .checks { left: 58px; top: 840px; list-style: none; font-size: 10.4px; color: var(--ink); }
  .checks li { display: flex; align-items: center; gap: 6px; height: 20.5px; }
  .btn { height: 26px; width: 88px; background: var(--orange); color: var(--white);
    font-family: 'Raleway', sans-serif; font-weight: 700; font-size: 10.5px;
    display: flex; align-items: center; justify-content: center; }
  .vsep { left: 547px; top: 730px; width: 1px; height: 200px; background: #ececec; }

  /* Inquiry */
  .inquiry-title { left: 581px; top: 729px; }
  .field { left: 581px; width: 223px; height: 23px; border: 1px solid #cfcfcf; background: var(--white);
    font-size: 9px; font-weight: 700; color: #6a6a6a; padding: 6px 9px; }

  /* Footer */
  .footer { left: 0; top: 972px; width: 861px; height: 196px; background: var(--footer); }
  .foot-head { font-family: 'Raleway', sans-serif; font-weight: 600; font-size: 13px; color: var(--white); }
  .foot-rule { height: 0; border-top: 1px dotted var(--footer-line); }
  .foot-links { list-style: none; font-size: 9.6px; color: #e4e4e4; }
  .foot-links li { height: 21.5px; display: flex; align-items: center; gap: 7px; }
  .foot-links li::before { content: "›"; color: var(--orange); font-size: 10px; }
  .foot-links .current { color: var(--orange); }
  .contact-row { left: 217px; display: flex; gap: 6px; font-size: 9.6px; color: #f0f0f0; line-height: 12px; }
  .colsep { top: 1010px; width: 1px; height: 128px; background: #474747; }
  .map { left: 453px; top: 1045px; width: 127px; height: 94px; border: 3px solid #e9e9e9;
    background: linear-gradient(135deg, #e8e2cf, #d8e0c9 55%, #c9d6e4); }
  .foot-brand { left: 665px; top: 1050px; width: 140px; text-align: center;
    font-family: 'Raleway', sans-serif; font-weight: 800; font-size: 16px; color: var(--white); line-height: 20px; letter-spacing: .5px; }
  .socials { left: 655px; top: 1118px; width: 160px; display: flex; justify-content: center; gap: 8px;
    font-size: 8.5px; color: var(--white); }
  .socials span { display: flex; align-items: center; gap: 3px; }
  .socials i { width: 9px; height: 9px; border-radius: 50%; background: var(--orange); display: inline-block; }
  .copyright { left: 0; top: 1168px; width: 861px; height: 32px; background: var(--orange);
    color: var(--white); font-size: 10px; display: flex; align-items: center; justify-content: center; }
</style>
</head>
<body>

<!-- Hero -->
<div class="abs hero" role="img" aria-label="Sunlit riverside promenade with lamp posts and a couple on a bench"></div>
<div class="abs hero-glow"></div>
<div class="abs brand"><span class="brand-square"></span>HALBROOK VIDEO</div>
<nav class="abs nav">
  <span class="active">HOME</span><span>ABOUT US</span><span>SERVICES</span><span>VIDEO GALLERY</span><span>CONTACT US</span>
</nav>
<h1 class="abs headline">Our Business Is Producing Videos For Companies,<br>Organizations And Not-for-profit Charities</h1>
<svg class="abs arrow" style="left:21px" width="26" height="46" viewBox="0 0 26 46"><path d="M24 1 L2 23 L24 45" fill="none" stroke="#fff" stroke-width="1.6"/></svg>
<svg class="abs arrow" style="left:814px" width="26" height="46" viewBox="0 0 26 46"><path d="M2 1 L24 23 L2 45" fill="none" stroke="#fff" stroke-width="1.6"/></svg>

<!-- Services -->
<section class="abs services">
  <h2 class="abs section-title"><span>OUR</span> SERVICES</h2>
  <div class="abs divider" style="left:327px;width:91px"></div>
  <div class="abs divider-mark"></div>
  <div class="abs divider" style="left:442px;width:93px"></div>

  <div class="abs tile" style="left:77px">
    <svg width="42" height="48" viewBox="0 0 42 48"><rect x="4" y="6" width="34" height="40" rx="4" fill="none" stroke="#8cc63f" stroke-width="4"/><path d="M12 18h18M12 25h18M12 32h18M12 39h12" stroke="#8cc63f" stroke-width="2.5"/></svg>
  </div>
  <div class="abs tile" style="left:227px">
    <svg width="50" height="46" viewBox="0 0 50 46"><rect x="3" y="8" width="34" height="34" fill="none" stroke="#7b3f98" stroke-width="4"/><circle cx="13" cy="32" r="4" fill="#7b3f98"/><path d="M20 36 L26 26 L32 36Z" fill="#7b3f98"/><path d="M24 24 L44 4 L48 8 L28 28 Z" fill="#7b3f98"/></svg>
  </div>
  <div class="abs tile" style="left:377px">
    <svg width="50" height="42" viewBox="0 0 50 42"><circle cx="10" cy="9" r="7" fill="none" stroke="#e8262c" stroke-width="4"/><circle cx="27" cy="9" r="7" fill="none" stroke="#e8262c" stroke-width="4"/><rect x="2" y="18" width="32" height="22" rx="2" fill="#e8262c"/><path d="M36 28 L48 18 V40 Z" fill="#e8262c"/></svg>
  </div>
  <div class="abs tile" style="left:526px">
    <svg width="44" height="46" viewBox="0 0 44 46"><path d="M3 10 L40 3 L41 12 L4 19Z" fill="#2e3f94"/><rect x="3" y="20" width="38" height="24" rx="3" fill="#2e3f94"/><rect x="7" y="27" width="30" height="2" fill="#fff"/><rect x="7" y="34" width="30" height="2" fill="#fff"/></svg>
  </div>
  <div class="abs tile" style="left:676px">
    <svg width="50" height="48" viewBox="0 0 50 48"><rect x="3" y="14" width="34" height="32" fill="none" stroke="#f26522" stroke-width="4"/><path d="M3 30h34M20 14v32" stroke="#f26522" stroke-width="3"/><circle cx="43" cy="6" r="4" fill="none" stroke="#f26522" stroke-width="2.5"/><circle cx="43" cy="20" r="4" fill="none" stroke="#f26522" stroke-width="2.5"/><path d="M40 9 L28 20 M40 17 L28 10" stroke="#f26522" stroke-width="2.5"/></svg>
  </div>

  <div class="abs tile-label" style="left:55px">WRITING</div>
  <div class="abs tile-label" style="left:205px">PLANNING</div>
  <div class="abs tile-label" style="left:355px">PRODUCING</div>
  <div class="abs tile-label" style="left:510px">DIRECTING FILMING</div>
  <div class="abs tile-label" style="left:654px">EDITING VIDEOS</div>
</section>

<!-- Welcome -->
<div class="abs welcome-mark"></div>
<h2 class="abs section-title welcome-title"><span>WELCOME TO</span> HALBROOK VIDEO</h2>
<div class="abs rule" style="left:57px;top:760px;width:465px"></div>
<p class="abs intro">Lorem ipsum dolor sit amet, consectetuer adipiscing elit, sed diam nonummy nibh euismod tincidunt ut laoreet dolore magna aliquam erat volutpat. Ut wisi enim ad minim veniam, quis nostrud exerci tation laoreet dolore magna aliquam erat volutpat. Ut wisi enim ad minim veniam, quis nostrud exerci tation ullamcorper suscipit lobortis nisl ut aliquip ex ea commodo consequat.</p>
<ul class="abs checks">
  <li><svg width="9" height="8" viewBox="0 0 9 8"><path d="M1 4 L3.5 7 L8 1" fill="none" stroke="#f26522" stroke-width="1.8"/></svg>Lorem ipsum dolor sit amet, consectetuer adipiscing elit</li>
  <li><svg width="9" height="8" viewBox="0 0 9 8"><path d="M1 4 L3.5 7 L8 1" fill="none" stroke="#f26522" stroke-width="1.8"/></svg>Lorem ipsum dolor sit amet consectetuer</li>
  <li><svg width="9" height="8" viewBox="0 0 9 8"><path d="M1 4 L3.5 7 L8 1" fill="none" stroke="#f26522" stroke-width="1.8"/></svg>Lorem ipsum dolor sit amet consectetuer adipiscing</li>
</ul>
<div class="abs btn" style="left:57px;top:912px">READ MORE</div>
<div class="abs vsep"></div>

<!-- Quick inquiry -->
<h2 class="abs section-title inquiry-title"><span>QUICK</span> INQUIRY</h2>
<div class="abs rule" style="left:581px;top:760px;width:170px"></div>
<div class="abs field" style="top:773px">First Name</div>
<div class="abs field" style="top:800px">Phone</div>
<div class="abs field" style="top:827px">Email</div>
<div class="abs field" style="top:854px;height:43px">Message</div>
<div class="abs btn" style="left:581px;top:912px">SUBMIT</div>

<!-- Footer -->
<footer class="abs footer"></footer>
<h3 class="abs foot-head" style="left:60px;top:1012px">Quick Links</h3>
<div class="abs foot-rule" style="left:60px;top:1036px;width:90px"></div>
<ul class="abs foot-links" style="left:60px;top:1041px">
  <li class="current">Home</li><li>About Us</li><li>Services</li><li>Video Gallery</li><li>Contact Us</li>
</ul>
<div class="abs colsep" style="left:185px"></div>

<h3 class="abs foot-head" style="left:217px;top:1012px">Contact Details</h3>
<div class="abs foot-rule" style="left:217px;top:1036px;width:170px"></div>
<div class="abs contact-row" style="top:1047px">
  <svg width="8" height="11" viewBox="0 0 8 11"><path d="M4 11 C1 7 0 5.5 0 4 A4 4 0 0 1 8 4 C8 5.5 7 7 4 11Z" fill="#f26522"/><circle cx="4" cy="4" r="1.5" fill="#3b3b3b"/></svg>
  <div>HALBROOK VIDEO<br>laoreetmok laoreet dol magnak<br>aliquam PG Feugait.</div>
</div>
<div class="abs foot-rule" style="left:217px;top:1092px;width:170px"></div>
<div class="abs contact-row" style="top:1101px">
  <svg width="10" height="10" viewBox="0 0 10 10"><path d="M2 0 L4 2.5 L3 4 C4 6 5 7 6 7 L7.5 6 L10 8 L8.5 10 C4 10 0 6 0 1.5Z" fill="#f26522"/></svg>
  <div>555 - 014 - 2290</div>
</div>
<div class="abs foot-rule" style="left:217px;top:1122px;width:170px"></div>
<div class="abs contact-row" style="top:1131px">
  <svg width="10" height="8" viewBox="0 0 10 8"><rect width="10" height="8" fill="#f26522"/><path d="M0 0 L5 4.5 L10 0" fill="none" stroke="#3b3b3b" stroke-width="1"/></svg>
  <div>info@halbrookvideo.com</div>
</div>
<div class="abs colsep" style="left:420px"></div>

<h3 class="abs foot-head" style="left:452px;top:1012px">Location Map</h3>
<div class="abs foot-rule" style="left:452px;top:1036px;width:130px"></div>
<div class="abs map" role="img" aria-label="Street map showing the studio location"></div>
<div class="abs colsep" style="left:613px"></div>

<div class="abs foot-brand">HALBROOK<br>VIDEO</div>
<div class="abs socials">
  <span><i></i>Circlo</span><span><i></i>Chirpa</span><span><i></i>Proflink</span>
</div>

<div class="abs copyright">Copyright © 2015 HALBROOK VIDEO. All Right Reserved.</div>

</body>
</html>
```